Tov Fest Falcons

We are party planning business. We are a team of established individuals and business in party stream businesses like DJ, Caterers, Party supplies, Kids parties, Events & Private Parties and much more. So basically me and business collaborate a team of business or individuals to do clients party in the best way possible.

Target Market(s)

majority of them 16 to 30 -60% to 70 % and 30 to 40 year olds- 30% to 40 %

Industry/Entity Type

Party Planning

Contact Information for Business Card

Tov
Owner & Manager
0481927354
tovfestfalcons@mailbright.example

Requirements
Must have
• front side : Logo and list of services we provide
DJ's, Catering,All party supplies, Tinyvolta and more...just to show what the business is about when anyone looks at the card and at the rear side my details which are already provided.
Should not have
• Dont make it look we do kids party which is just one of the things we do but don't make my business card look like kids party specialist make it more connecting to youngsters and older crowd more

```html
<!DOCTYPE html>
<html lang="en">
<head>
<meta charset="utf-8">
<title>Tov Fest Falcons – Business Card</title>
<link rel="stylesheet" href="https://fonts.googleapis.com/css2?family=Quicksand:wght@500;700&display=swap">
<style>
  :root {
    --backdrop: #e7e4df;
    --card: #f3f2ef;
    --card-edge: #dcdad5;
    --bar: #1c2a29;
    --bar-rule: #d6d6d6;
    --accent-red: #e1403e;
    --ink: #1b1b1b;
  }
  * { box-sizing: border-box; margin: 0; padding: 0; }
  html, body { width: 1200px; height: 960px; overflow: hidden; }
  body {
    background: var(--backdrop);
    font-family: "Quicksand", sans-serif;
    position: relative;
  }
  .card {
    position: absolute;
    left: 300px;
    width: 600px;
    height: 340px;
    background: var(--card);
    border: 1px solid var(--card-edge);
    box-shadow: 0 6px 18px rgba(0,0,0,0.12);
    overflow: hidden;
  }
  .card--front { top: 100px; }
  .card--back { top: 520px; }

  .brand {
    position: absolute;
    left: 40px;
    top: 0;
    width: 280px;
    height: 100%;
    display: flex;
    flex-direction: column;
    align-items: center;
    justify-content: center;
    text-align: center;
  }
  .brand__dot {
    width: 54px;
    height: 54px;
    border-radius: 50%;
    background: var(--accent-red);
    margin-bottom: 16px;
  }
  .brand__name {
    font-weight: 700;
    font-size: 34px;
    line-height: 1.05;
    color: var(--accent-red);
  }
  .brand__tagline {
    margin-top: 14px;
    font-weight: 700;
    font-size: 14px;
    line-height: 1.3;
    color: var(--ink);
  }

  .bar-list {
    position: absolute;
    right: 0;
    list-style: none;
    width: 240px;
  }
  .card--front .bar-list { top: 64px; }
  .card--back .bar-list { top: 76px; width: 250px; }
  .bar-list__item {
    height: 36px;
    background: var(--bar);
    border-top: 3px solid var(--bar-rule);
    color: var(--accent-red);
    font-weight: 500;
    font-size: 18px;
    line-height: 33px;
    padding-left: 12px;
    white-space: nowrap;
  }
  .bar-list__item:last-child { border-bottom: 3px solid var(--bar-rule); height: 39px; }
  .bar-list--centered .bar-list__item { text-align: center; padding-left: 0; }
  .bar-list__item--email { font-size: 13.5px; }
</style>
</head>
<body>
  <section class="card card--front" aria-label="Business card front">
    <div class="brand">
      <span class="brand__dot"></span>
      <p class="brand__name">Tov Fest<br>Falcons</p>
      <p class="brand__tagline">Delivering The Ultimate<br>Treasures To Your Party</p>
    </div>
    <ul class="bar-list">
      <li class="bar-list__item">DJ's,</li>
      <li class="bar-list__item">Catering,</li>
      <li class="bar-list__item">All party supplies,</li>
      <li class="bar-list__item">Tinyvolta,</li>
      <li class="bar-list__item">and more...</li>
    </ul>
  </section>

  <section class="card card--back" aria-label="Business card back">
    <div class="brand">
      <span class="brand__dot"></span>
      <p class="brand__name">Tov Fest<br>Falcons</p>
      <p class="brand__tagline">Delivering The Ultimate<br>Treasures To Your Party</p>
    </div>
    <ul class="bar-list bar-list--centered">
      <li class="bar-list__item">Tov</li>
      <li class="bar-list__item">owner &amp; manager</li>
      <li class="bar-list__item">0481927354</li>
      <li class="bar-list__item bar-list__item--email">tovfestfalcons@mailbright.example</li>
    </ul>
  </section>
</body>
</html>
```